Visitenkarten für den Verkauf mediterraner Pflanzen
Zielgruppe
Verkauf winterharter mediterraner Pflanzen
Aufgabenstellung
Die Farben von der Homepage und eventuell die Schriftarten sollten übernommen werden um ein einheitliches Erscheinungsbild zu erzeugen

```html
<!DOCTYPE html>
<html lang="de">
<head>
<meta charset="utf-8">
<title>Verdalia – Visitenkarten</title>
<link rel="stylesheet" href="https://fonts.googleapis.com/css2?family=Saira+Semi+Condensed:wght@400;600&family=Saira+Condensed:wght@600&display=swap">
<style>
  :root {
    --stage: #a9c7b5;
    --card-dark: #2d4b43;
    --card-dark-deep: #25403a;
    --card-light: #8d9a93;
    --leaf: #4d6b5d;
    --leaf-deep: #3a5549;
    --accent: #5fae8e;
    --ink-light: #eef3ef;
    --ink-dark: #2b3440;
  }
  * { box-sizing: border-box; margin: 0; padding: 0; }
  html, body { width: 1200px; height: 892px; overflow: hidden; }
  body {
    background: var(--stage);
    font-family: "Saira Semi Condensed", sans-serif;
    position: relative;
  }
  .card {
    position: absolute;
    top: 296px;
    width: 520px;
    height: 300px;
    overflow: hidden;
    box-shadow: 0 18px 40px rgba(40, 80, 65, 0.25);
  }

  /* Rückseite: Kontaktdaten */
  .card--back {
    left: 50px;
    background: linear-gradient(160deg, var(--card-dark) 0%, var(--card-dark-deep) 100%);
  }
  .card--back .leaf-texture {
    position: absolute; inset: 0;
    background: radial-gradient(ellipse at 70% 10%, rgba(255,255,255,0.06), transparent 60%);
  }
  .contact {
    position: absolute;
    left: 110px; top: 62px;
    display: grid;
    grid-template-columns: 110px 1px auto;
    column-gap: 22px;
  }
  .contact__labels, .contact__values {
    display: flex; flex-direction: column;
  }
  .contact__labels {
    text-align: right;
    font-family: "Saira Condensed", sans-serif;
    font-weight: 600;
    color: var(--accent);
    font-size: 15px;
    letter-spacing: 0.04em;
    text-transform: uppercase;
    line-height: 22px;
    padding-top: 2px;
  }
  .contact__labels .gap { height: 22px; }
  .contact__rule { background: var(--accent); height: 104px; margin-top: 6px; }
  .contact__values {
    color: var(--ink-light);
    font-size: 15px;
    line-height: 20px;
    padding-top: 14px;
  }
  .contact__values span + span { margin-top: 6px; }
  .contact__values .address { line-height: 18px; }
  .social {
    position: absolute;
    left: 182px; top: 222px;
    display: flex; gap: 26px;
  }
  .social__dot {
    width: 16px; height: 16px; border-radius: 50%;
    border: 1.5px solid var(--accent);
  }

  /* Vorderseite: Name und Claim */
  .card--front {
    left: 630px;
    background: var(--card-light);
  }
  .card--front .leaf-photo {
    position: absolute; inset: 0;
    background:
      radial-gradient(ellipse 70% 55% at 60% 85%, var(--leaf-deep) 0%, transparent 70%),
      radial-gradient(ellipse 80% 60% at 85% 40%, var(--leaf) 0%, transparent 70%),
      linear-gradient(180deg, #8f9c95 0%, #7d8e85 55%, #5a7465 100%);
  }
  .brand {
    position: absolute;
    left: 40px; top: 66px;
    font-family: "Saira Semi Condensed", sans-serif;
    font-weight: 600;
    color: var(--ink-dark);
    font-size: 24px;
    line-height: 28px;
  }
  .claim {
    position: absolute;
    left: 200px; top: 148px;
    width: 280px;
    text-align: center;
    color: var(--ink-light);
    font-size: 17px;
    line-height: 21px;
  }
</style>
</head>
<body>

  <section class="card card--back" aria-label="Visitenkarte Rückseite">
    <div class="leaf-texture" role="img" aria-label="Dunkelgrünes Foto eines Palmblatts als Hintergrund"></div>
    <div class="contact">
      <div class="contact__labels">
        <span>Adresse</span>
        <span class="gap"></span>
        <span>Web</span>
        <span>Telefon</span>
        <span>E-Mail</span>
      </div>
      <div class="contact__rule"></div>
      <div class="contact__values">
        <span class="address">Birkenfeld 214<br>8100, Österreich</span>
        <span>www.verdalia.at</span>
        <span>+43 (0)660 5823419</span>
        <span>office@verdalia.at</span>
      </div>
    </div>
    <div class="social" aria-label="Soziale Netzwerke">
      <span class="social__dot"></span>
      <span class="social__dot"></span>
      <span class="social__dot"></span>
    </div>
  </section>

  <section class="card card--front" aria-label="Visitenkarte Vorderseite">
    <div class="leaf-photo" role="img" aria-label="Nahaufnahme eines grünen Fächerpalmblatts"></div>
    <p class="brand">Verdalia</p>
    <p class="claim">Dein Spezialist für Palmen<br>und exotische Pflanzen</p>
  </section>

</body>
</html>
```